Lanterne architecture business cards

We are a new company based in New Zealand. We Specialize in High end Luxury Residential Architecture.

Every home is bespoke and is designed to each clients individual requirements and needs.

I like to design buildings that inspire people through light and form while offering a high level of comfort and usability.

Lines of sight, proportion and balance are fundamental to the spaces I create.
Updates

August 5th is current deadline - Today's date is the 13th of August.

Target Market(s)

New Zealanders who want a custom individual home design, typically 30-65 year old males and females

Industry/Entity Type

Architecture

Contact Information for Business Card

Director - Derek Tolson
Contact Number - 0279164073
Email - info@lanternearchitecture-example.co.nz
Webstie - www.lanternearchitecture-example.co.nz
Social Media - @lanternearchitecture

Font styles to use
Sans Serif

Requirements
Must have
• Logo (Both Sides)
Website
Email
Contact Number
Social Media

Nice to have
• Texture
Should not have
• More than 3 colours - typically I would've thought 2 would be good to match the logo.

```html
<!DOCTYPE html>
<html lang="en">
<head>
<meta charset="utf-8">
<title>Lanterne architecture business cards</title>
<link rel="stylesheet" href="https://fonts.googleapis.com/css2?family=Josefin+Sans:wght@300;400;600&display=swap">
<style>
  :root {
    --backdrop: #4a4a4a;
    --card: #2b2b2d;
    --ink: #ededed;
    --ink-soft: #c9c9c9;
  }
  * { margin: 0; padding: 0; box-sizing: border-box; }
  html, body {
    width: 800px;
    height: 1200px;
    overflow: hidden;
    background: var(--backdrop);
    font-family: "Josefin Sans", sans-serif;
    color: var(--ink);
  }
  .sheet {
    position: relative;
    width: 800px;
    height: 1200px;
  }
  .card {
    position: absolute;
    left: 80px;
    width: 640px;
    height: 356px;
    background: var(--card);
    box-shadow: 0 10px 30px rgba(0,0,0,0.35);
  }
  .card--front { top: 150px; }
  .card--back { top: 694px; }

  /* Wordmark */
  .wordmark {
    position: absolute;
    font-weight: 300;
    color: var(--ink);
    text-transform: uppercase;
    line-height: 1;
  }
  .wordmark__name { display: block; }
  .wordmark__sub { display: block; }

  .card--front .mark-dot {
    position: absolute;
    left: 304px;
    top: 92px;
    width: 32px;
    height: 32px;
    border: 2px solid var(--ink-soft);
    border-radius: 50%;
  }
  .card--front .wordmark {
    left: 0;
    right: 0;
    top: 150px;
    text-align: center;
  }
  .card--front .wordmark__name {
    font-size: 34px;
    letter-spacing: 0.42em;
    margin-right: -0.42em;
  }
  .card--front .wordmark__sub {
    margin-top: 10px;
    font-size: 12px;
    letter-spacing: 1.25em;
    margin-right: -1.25em;
  }

  /* Back details */
  .contact {
    position: absolute;
    left: 44px;
    top: 36px;
    font-size: 16px;
    line-height: 1.45;
    color: var(--ink);
  }
  .contact__name {
    font-weight: 600;
    font-size: 14px;
    letter-spacing: 0.3em;
    text-transform: uppercase;
  }
  .contact__role {
    font-weight: 300;
    font-size: 15px;
    margin-bottom: 10px;
  }
  .contact__line { font-weight: 300; }
  .contact__label {
    display: inline-block;
    width: 18px;
    font-weight: 600;
  }
  .contact__handle { font-weight: 300; margin-top: 2px; }

  .card--back .wordmark {
    left: 44px;
    top: 244px;
  }
  .card--back .wordmark__name {
    font-size: 46px;
    letter-spacing: 0.42em;
  }
  .card--back .wordmark__sub {
    margin-top: 10px;
    font-size: 13px;
    letter-spacing: 1.9em;
  }
</style>
</head>
<body>
  <main class="sheet">
    <section class="card card--front" aria-label="Card front">
      <span class="mark-dot" aria-hidden="true"></span>
      <div class="wordmark">
        <span class="wordmark__name">Lanterne</span>
        <span class="wordmark__sub">Architecture</span>
      </div>
    </section>

    <section class="card card--back" aria-label="Card back">
      <div class="contact">
        <p class="contact__name">Derek Tolson</p>
        <p class="contact__role">director</p>
        <p class="contact__line"><span class="contact__label">P</span>0279 164 073</p>
        <p class="contact__line"><span class="contact__label">E</span>info@lanternearchitecture-example.co.nz</p>
        <p class="contact__line"><span class="contact__label">W</span>www.lanternearchitecture-example.co.nz</p>
        <p class="contact__handle">@lanternearchitecture</p>
      </div>
      <div class="wordmark">
        <span class="wordmark__name">Lanterne</span>
        <span class="wordmark__sub">Architecture</span>
      </div>
    </section>
  </main>
</body>
</html>
```